Lindenfield Advocacy Learning Forums
Icon Set
We wish to design an icon set to be used in printed brochures as well as our website and other marketing materials.
Law
Professional - Lawyers. LALF provides legal training and education seminar for lawyers.
LALF organises and presents regular legal professional seminars throughout Australia. Our marketing is heavily based on direct mail. When we schedule our seminars we design and print brochures and send them to all lawyers that are close to the location of the seminars.
All lawyers in Australia are required to attend a specified number of hours of continuing education seminars each year. For every hour of attendance, they can gain 1 point and they usually need to accumulate 10-20 points per year.
In most cases there are also compulsory areas that must be covered. Each State has different requirements, but there are four main compulsory areas:
1. Legal Ethics
2. Practice Management or Business Skills
3. Professional Skills
4. Substantive Law
There is also an additional subject area which is used in one location (Sydney) – this is for OH & S, Employment Law, Equal Opportunity and Discrimination Law.
We always designate how many points (or hours) a lawyer will get by attending one of our seminars and in which compulsory area they will get the points.
What we need is an icon for each of the four main areas. Each icon should ideally be recognizable with the particular compulsory area and be a different colour. We would also like an icon for the additional subject area in Sydney, but this is not essential.
Also, it would be ideal if the points and/or description of the compulsory area could be incorporated within the icon graphic. However, if this is not possible, then this can be done as text under the icon or to the side.
The icon does not need to be any particular size – it could be square, round, rectangle or anything else. But, please remember the context we will be using it in. The main use will be in the marketing brochures. But we would also like to use it on our website and other media as required.
I will also need to be able to edit each icon as the descriptions of the compulsory subjects differ slightly between the States. I will also need to be able to change the number of points. Ideally, I should be able to edit the icons using Adobe Illustrator.
I will upload several examples of our marketing brochures which show how we currently designate points/compulsory areas for each seminar. The icons we use at the moment are a set of stock-icons I purchased on the web. However, these icons were never ideal and we would like something that is specifically designed for our purposes.
Also, if you look at the back panel of each brochure (panel 5 on the first page), there is a description of what each icon represents and more information on the compulsory subjects. This information is different for each State.
I will also upload some examples of icons used by some of our competitors. Please note that none of these examples actually specify the number of points within the graphic. This is not ideal. I think a clear number should be included in the graphic. For example, if the seminar has 3 points – then a clear “3” should stand out in the icon.
Finally, please also note that I wish to redesign the template we use for our marketing brochures. I will create a separate project for this, but you may wish to consider submitting a design for this as well. Please see this project for the specific details.
Example of Sydney Brochure
Example of Melbourne Brochure
Example of Brisbane Brochure
Example of Perth Brochure

```html
<!DOCTYPE html>
<html lang="en">
<head>
<meta charset="utf-8">
<title>Lindenfield Advocacy Learning Forums – CPD Area Icons</title>
<link href="https://fonts.googleapis.com/css2?family=PT+Sans:wght@400;700&display=swap" rel="stylesheet">
<style>
  :root {
    --page: #ffffff;
    --text: #ffffff;

    --ethics-base: #1a6fc0;
    --ethics-dark: #125a9e;
    --ethics-gloss: #6b9fdc;
    --ethics-points: #4f93d6;

    --practice-base: #d9481f;
    --practice-dark: #b83a16;
    --practice-gloss: #e8876a;
    --practice-points: #ef7a55;

    --skills-base: #1b9141;
    --skills-dark: #147634;
    --skills-gloss: #5cb878;
    --skills-points: #46b067;

    --law-base: #7e1b74;
    --law-dark: #64135c;
    --law-gloss: #a66aa1;
    --law-points: #9c4894;
  }

  * { box-sizing: border-box; margin: 0; padding: 0; }

  html, body {
    width: 1200px;
    height: 871px;
    overflow: hidden;
    background: var(--page);
    font-family: "PT Sans", "Helvetica Neue", Arial, sans-serif;
  }

  .icon-set {
    position: relative;
    width: 1200px;
    height: 871px;
  }

  .area-badge {
    position: absolute;
    left: 125px;
    width: 950px;
    height: 115px;
    border-radius: 12px;
    overflow: hidden;
    display: flex;
    color: var(--text);
    background: var(--base);
    border: 2px solid var(--dark);
    box-shadow: 0 2px 3px rgba(0,0,0,0.15);
  }

  .area-badge--ethics   { top: 113px; --base: var(--ethics-base);   --dark: var(--ethics-dark);   --gloss: var(--ethics-gloss);   --points: var(--ethics-points); }
  .area-badge--practice { top: 288px; --base: var(--practice-base); --dark: var(--practice-dark); --gloss: var(--practice-gloss); --points: var(--practice-points); }
  .area-badge--skills   { top: 463px; --base: var(--skills-base);   --dark: var(--skills-dark);   --gloss: var(--skills-gloss);   --points: var(--skills-points); }
  .area-badge--law      { top: 638px; --base: var(--law-base);      --dark: var(--law-dark);      --gloss: var(--law-gloss);      --points: var(--law-points); }

  .area-badge__symbol {
    width: 118px;
    flex: none;
    background: linear-gradient(180deg, var(--gloss) 0%, var(--base) 60%);
    opacity: 0.95;
  }

  .area-badge__name {
    flex: 1;
    position: relative;
    display: flex;
    align-items: flex-end;
    padding: 0 0 22px 10px;
    font-size: 43px;
    line-height: 1;
    background: linear-gradient(180deg, var(--gloss) 0%, var(--gloss) 48%, var(--base) 48%, var(--base) 100%);
  }

  .area-badge__points {
    width: 245px;
    flex: none;
    display: flex;
    flex-direction: column;
    align-items: center;
    justify-content: center;
    background: linear-gradient(180deg, var(--gloss) 0%, var(--gloss) 48%, var(--points) 48%, var(--points) 100%);
    border-left: 1px solid rgba(255,255,255,0.15);
  }

  .area-badge__value {
    font-size: 52px;
    line-height: 0.95;
  }

  .area-badge__unit {
    font-size: 22px;
    line-height: 1.1;
    margin-top: 2px;
  }
</style>
</head>
<body>
  <main class="icon-set">
    <div class="area-badge area-badge--ethics">
      <div class="area-badge__symbol" role="img" aria-label="Scales of justice symbol"></div>
      <div class="area-badge__name">Legal Ethics</div>
      <div class="area-badge__points">
        <span class="area-badge__value">3.25</span>
        <span class="area-badge__unit">CDP Points</span>
      </div>
    </div>

    <div class="area-badge area-badge--practice">
      <div class="area-badge__symbol" role="img" aria-label="Two business people with briefcases symbol"></div>
      <div class="area-badge__name">Practice Management</div>
      <div class="area-badge__points">
        <span class="area-badge__value">3.25</span>
        <span class="area-badge__unit">CDP Points</span>
      </div>
    </div>

    <div class="area-badge area-badge--skills">
      <div class="area-badge__symbol" role="img" aria-label="Briefcase symbol"></div>
      <div class="area-badge__name">Professional Skills</div>
      <div class="area-badge__points">
        <span class="area-badge__value">3.25</span>
        <span class="area-badge__unit">CDP Points</span>
      </div>
    </div>

    <div class="area-badge area-badge--law">
      <div class="area-badge__symbol" role="img" aria-label="Judge with gavel symbol"></div>
      <div class="area-badge__name">Substantive Law</div>
      <div class="area-badge__points">
        <span class="area-badge__value">3.25</span>
        <span class="area-badge__unit">CDP Points</span>
      </div>
    </div>
  </main>
</body>
</html>
```